Self Defence Seminar Flyer

Need a flyer that will sell a seminar that will teach self defence techniques to customers. Needs to have a good image that will remind people about the dangerous world. The seminar is for men and women.

Needs to look professional.

I have attached the previous flyer we used. needs same information except without the same date and time for seminar.

Target Market(s)

Male and Females interested in learning how to defend themselves or family

Industry/Entity Type

Defence

Requirements
Must have
• A Image that reminds people of a dangerous situation

```html
<!DOCTYPE html>
<html lang="en">
<head>
<meta charset="utf-8">
<title>Self Defense Seminar Flyer</title>
<link href="https://fonts.googleapis.com/css2?family=Black+Ops+One&family=Ubuntu:wght@500;700&family=Open+Sans:wght@400;600;700&display=swap" rel="stylesheet">
<style>
  :root{
    --page:#e9e9e9;
    --ink:#0b0b0b;
    --ink-soft:#1c1a18;
    --orange:#f08a1c;
    --orange-deep:#e2661a;
    --red:#b3241c;
    --red-deep:#8e1a14;
    --white:#ffffff;
    --silver-hi:#f4f1ea;
    --silver-lo:#a9a397;
    --button-ink:#2a2a2a;
  }
  *{box-sizing:border-box;margin:0;padding:0}
  html,body{width:1200px;height:1157px;overflow:hidden;background:var(--page)}
  .flyer{
    position:absolute;left:200px;top:13px;width:800px;height:1131px;
    background:radial-gradient(ellipse at 50% 70%,var(--ink-soft),var(--ink) 75%);
    overflow:hidden;font-family:"Open Sans",sans-serif;color:var(--white);
  }
  .title{
    position:absolute;top:28px;left:0;width:100%;text-align:center;
    font-family:"Black Ops One",sans-serif;font-size:62px;letter-spacing:1px;
    background:linear-gradient(90deg,var(--orange) 0%,var(--orange-deep) 45%,var(--red) 100%);
    -webkit-background-clip:text;background-clip:text;color:transparent;
  }
  .hero{
    position:absolute;top:112px;left:0;width:100%;height:470px;
    background:
      linear-gradient(180deg,rgba(11,11,11,0) 60%,var(--ink) 100%),
      linear-gradient(100deg,#56606a 0%,#3a3f48 35%,#7a6148 65%,#b7895a 85%,#5b3a24 100%);
  }
  .headline{position:absolute;left:40px;top:540px;width:730px;font-family:"Ubuntu",sans-serif;font-weight:700}
  .headline .lead{color:var(--orange);font-size:34px;padding-left:10px}
  .headline .lead em{font-style:normal;font-size:50px}
  .headline .tail{color:var(--red);font-size:34px;text-align:right;margin-top:-4px}
  .headline .tail em{font-style:normal;font-size:46px}
  .intro{position:absolute;left:40px;top:650px;width:380px;text-align:center}
  .intro p.body{font-size:22px;line-height:1.3}
  .intro p.skill{color:var(--orange);font-family:"Ubuntu",sans-serif;font-weight:700;font-size:23px;line-height:1.25;margin-top:14px}
  .intro h3{color:var(--orange);font-family:"Ubuntu",sans-serif;font-size:32px;margin-top:14px;line-height:1.1}
  .intro p.range{color:var(--red);font-family:"Ubuntu",sans-serif;font-weight:700;font-size:23px;line-height:1.15}
  .signup{
    position:absolute;left:70px;top:920px;width:270px;height:54px;border-radius:8px;
    background:linear-gradient(180deg,var(--silver-hi),var(--silver-lo));
    box-shadow:0 6px 14px rgba(0,0,0,.6);
    font-family:"Ubuntu",sans-serif;font-weight:700;font-style:italic;font-size:30px;
    color:var(--button-ink);text-align:center;line-height:54px;
  }
  .website{position:absolute;left:40px;top:1000px;width:400px;text-align:center;color:var(--orange);font-weight:700;font-size:20px}
  .location{position:absolute;left:40px;top:1040px;width:400px;text-align:center;font-size:15px;line-height:1.4}
  .details{
    position:absolute;left:440px;top:660px;width:330px;height:330px;padding:20px 16px;
    background:linear-gradient(180deg,var(--orange-deep),var(--orange) 60%,#f29a2a);
    color:var(--ink);text-align:center;
  }
  .details h2{font-family:"Ubuntu",sans-serif;color:var(--red-deep);font-size:52px;line-height:1}
  .details p{font-weight:700;font-size:17px;line-height:1.2}
  .details p.sub{font-size:15px;margin-top:6px}
  .details h4{font-family:"Ubuntu",sans-serif;color:var(--red-deep);font-size:23px;margin-top:14px;line-height:1}
  .details p.note{font-size:14px;line-height:1.15;font-weight:600}
  .cost{position:absolute;left:440px;top:1000px;width:330px;text-align:center;font-family:"Ubuntu",sans-serif;font-weight:700;font-size:26px;color:var(--orange)}
  .team{position:absolute;left:540px;top:1040px;width:130px;height:80px;text-align:center;font-family:"Open Sans",sans-serif;font-weight:700;color:var(--white)}
  .team .handle{font-size:12px;display:flex;align-items:center;justify-content:center;gap:5px}
  .team .handle span.mark{width:10px;height:10px;background:var(--white)}
  .team .name{font-size:24px;margin-top:10px}
</style>
</head>
<body>
<main class="flyer">
  <h1 class="title">SELF DEFENSE SEMINAR</h1>
  <div class="hero" role="img" aria-label="Photo of a hooded man following a worried woman along a street"></div>

  <div class="headline">
    <p class="lead">Being a <em>victim</em> is a topic</p>
    <p class="tail">people would like to <em>avoid</em></p>
  </div>

  <section class="intro">
    <p class="body">Unfortunately, we live in an increasingly dangerous society for men and woman alike.</p>
    <p class="skill">Learning to defend yourself is an important life skill</p>
    <h3>Effective &amp; Efficient</h3>
    <p class="range">Defend yourself in a range of situations</p>
  </section>

  <div class="signup">SIGN UP NOW</div>
  <p class="website">www.combatskillsacademy.com</p>
  <p class="location">Location - Combat Skills Academy Gym,<br>214, Harbour Rd. Millbrook NSW</p>

  <section class="details">
    <h2>2 HOURS</h2>
    <p>Learn simple and effective<br>SELF DEFENSE tactics</p>
    <p class="sub">Defend yourself or loved ones</p>
    <h4>Techniques &amp; Tactics</h4>
    <p class="note">as used in Law Enforcement,<br>Security and Military</p>
    <h4>Weapon Defense</h4>
    <p class="note">use of surroundings &amp; psychological<br>techniques taught</p>
  </section>

  <p class="cost">COST - $60</p>
  <div class="team">
    <p class="handle"><span class="mark"></span>/CSATEAM</p>
    <p class="handle"><span class="mark"></span>#CSATEAM</p>
    <p class="name">Team CSA</p>
  </div>
</main>
</body>
</html>
```